Steel Company / Iron Railing Business Card Template

We are a custom steel fabrication company located in Harlow Ridge, HR. In business since 1979, we recently developed a new logo, and we're looking for a business card design to help display the new logo and our business. The name of the company is Kelbrook Forge Co.. The Office Phone number is (610) 555-0143. We fabricate and install custom "wrought iron" railings on our residential side, we also fabricate and erect structural steel (think cranes and steel beams in buildings) on our commercial side. Looking to get a business card template designed. Something modern, but professional. Clear and easy to read. Front should have all business and employee information including phone number(s), email address, business information, etc. back should spotlight logo.

Industry/Entity Type

Construction / Home Improvement

Contact Information for Business Card

Business information is Kelbrook Forge Co., 48 Dunmore Ave Suite 3305, Harlow Ridge, HR 19074. Phone number is (610) 555-0143. Website is www.kelbrookforge.example Business card should be for "Tom Pelling" with the job title "Sales & Estimating" but be editable for other employees. Tom's phone number is (610) 555-0178

Colors

Designer to choose colors to be used in the design.

Requirements
Must have
• Modern Feel, Design should be sized for standard business card sizing 3.5" x 2" (88.9mm x 50.8mm)

```html
<!DOCTYPE html>
<html lang="en">
<head>
<meta charset="utf-8">
<title>Kelbrook Forge Co. — Business Card</title>
<link rel="stylesheet" href="https://fonts.googleapis.com/css2?family=Marcellus&family=Open+Sans:wght@400;600&display=swap">
<style>
  :root {
    --navy: #1f3a8f;
    --red: #d6343c;
    --ink: #3f3f44;
    --rule: #8d9cc4;
    --paper: #ffffff;
    --paper-shade: #eeeff1;
    --backdrop: #d9dadd;
    --rail-tone: #dfe3ec;
  }
  * { box-sizing: border-box; margin: 0; padding: 0; }
  html, body { width: 1200px; height: 900px; overflow: hidden; }
  body {
    background: var(--backdrop);
    font-family: "Open Sans", Arial, sans-serif;
    position: relative;
  }
  .card {
    position: absolute;
    width: 600px;
    height: 343px;
    background: linear-gradient(120deg, var(--paper) 0%, var(--paper-shade) 55%, var(--paper) 100%);
    box-shadow: 0 10px 28px rgba(0,0,0,.22);
    overflow: hidden;
  }
  .card--back { left: 300px; top: 80px; }
  .card--front { left: 300px; top: 470px; }

  .brand {
    display: flex;
    align-items: center;
    gap: 12px;
    font-family: "Marcellus", Georgia, serif;
    color: var(--navy);
    white-space: nowrap;
  }
  .brand__dot {
    border-radius: 50%;
    background: var(--red);
    flex: none;
  }
  .card--back .brand {
    position: absolute;
    left: 50%; top: 50%;
    transform: translate(-50%, -50%);
    font-size: 40px;
  }
  .card--back .brand__dot { width: 22px; height: 22px; }

  .card--front .brand {
    position: absolute;
    right: 34px; top: 38px;
    font-size: 26px;
  }
  .card--front .brand__dot { width: 14px; height: 14px; }

  .railing-art {
    position: absolute;
    right: 0; bottom: 0;
    width: 185px; height: 150px;
    background: linear-gradient(180deg, var(--rail-tone) 0%, rgba(223,227,236,.35) 100%);
  }

  .contact {
    position: absolute;
    left: 40px; bottom: 34px;
    width: 365px;
  }
  .contact__name {
    font-family: "Marcellus", Georgia, serif;
    color: var(--navy);
    font-size: 24px;
    font-weight: 400;
    letter-spacing: .5px;
  }
  .contact__title {
    color: var(--ink);
    font-size: 14px;
    margin-top: 2px;
    margin-bottom: 16px;
  }
  .contact__list { list-style: none; }
  .contact__item {
    display: flex;
    align-items: center;
    gap: 10px;
    color: var(--ink);
    font-size: 14px;
    line-height: 24px;
    white-space: nowrap;
  }
  .contact__icon { width: 15px; height: 15px; flex: none; }
  .contact__rule {
    border: 0;
    border-top: 1px solid var(--rule);
    margin: 8px 0 6px;
  }
</style>
</head>
<body>

<section class="card card--back" aria-label="Card back">
  <div class="brand">
    <span class="brand__dot"></span>
    <span class="brand__name">Kelbrook Forge Co.</span>
  </div>
</section>

<section class="card card--front" aria-label="Card front">
  <div class="brand">
    <span class="brand__dot"></span>
    <span class="brand__name">Kelbrook Forge Co.</span>
  </div>

  <div class="railing-art" role="img" aria-label="Faint wrought iron railing illustration"></div>

  <div class="contact">
    <h1 class="contact__name">TOM PELLING</h1>
    <p class="contact__title">Sales &amp; Estimating</p>
    <ul class="contact__list">
      <li class="contact__item">
        <svg class="contact__icon" viewBox="0 0 16 16" aria-hidden="true"><rect x="4" y="1" width="8" height="14" rx="1.5" fill="none" stroke="#d6343c" stroke-width="1.5"/><line x1="7" y1="12.5" x2="9" y2="12.5" stroke="#d6343c" stroke-width="1.3"/></svg>
        (610) 555-0178
      </li>
      <li class="contact__item">
        <svg class="contact__icon" viewBox="0 0 16 16" aria-hidden="true"><path d="M3 1.5l2.5 0 1.2 3.2-1.6 1.2a8 8 0 0 0 5 5l1.2-1.6 3.2 1.2v2.5c0 .8-.7 1.5-1.5 1.5A12.5 12.5 0 0 1 1.5 3c0-.8.7-1.5 1.5-1.5z" fill="#d6343c"/></svg>
        (610) 555-0143
      </li>
      <li class="contact__item">
        <svg class="contact__icon" viewBox="0 0 16 16" aria-hidden="true"><g fill="none" stroke="#d6343c" stroke-width="1.2"><circle cx="8" cy="8" r="6.5"/><ellipse cx="8" cy="8" rx="3" ry="6.5"/><line x1="1.5" y1="8" x2="14.5" y2="8"/><line x1="2.5" y1="4.5" x2="13.5" y2="4.5"/><line x1="2.5" y1="11.5" x2="13.5" y2="11.5"/></g></svg>
        www.kelbrookforge.example
      </li>
    </ul>
    <hr class="contact__rule">
    <p class="contact__item">
      <svg class="contact__icon" viewBox="0 0 16 16" aria-hidden="true"><path d="M8 1a5 5 0 0 0-5 5c0 3.8 5 9 5 9s5-5.2 5-9a5 5 0 0 0-5-5zm0 7a2 2 0 1 1 0-4 2 2 0 0 1 0 4z" fill="#d6343c"/></svg>
      48 Dunmore Ave Suite 3305, Harlow Ridge, HR 19074
    </p>
  </div>
</section>

</body>
</html>
```